Text Box for making an update on our website

We need an awesome "Text Box" so that our Users can make an amazing Post or update on our website or App.

Let's make something super duper like Pictavo, Friendloop, Chirr or Qmeld text box but a bit more amazing....

I've included our current desktop and Mobile "Text Box" which needs love :)

Our Text Box by default makes a Post "Private" the User can change it to "Public"

I have included what a final "Post" looks like on our site.

Could we incorporate a bit of the "Post" design into the "Create Post" design..... maybe make the header similar.

thanks

Morgan

Target Market(s)

Health Care, Hospitals, Caregivers, Nurses

Industry/Entity Type

Health Care

Font styles to use
Other font styles liked:
• Comfortaa

Requirements
Must have
• Our main colors are

#1D44B8 - Blue
#D85097 - Pink
Nice to have
• Super clean and simple. Happy and Easy to use
Should not have
• Complicated

Too many colors

```html
<!DOCTYPE html>
<html lang="en">
<head>
<meta charset="utf-8">
<title>Create Post – Mobile Text Box</title>
<link href="https://fonts.googleapis.com/css2?family=Roboto:wght@400;500;700&display=swap" rel="stylesheet">
<style>
  :root{
    --blue:#1D44B8;
    --blue-action:#1f47bc;
    --pink:#D85097;
    --pink-accent:#e0388f;
    --placeholder:#a9b8f6;
    --status-grey:#8a8a8c;
    --notice-grey:#808080;
    --ink:#111111;
    --white:#ffffff;
    --kb-bg:#0a0a0a;
    --key:#545454;
    --key-fn:#2b2b2b;
    --page:#ffffff;
  }
  *{box-sizing:border-box;margin:0;padding:0}
  html,body{width:1200px;height:1200px;overflow:hidden;background:var(--page)}
  body{position:relative;font-family:"Roboto",Arial,sans-serif}

  .phone-screen{
    position:absolute;left:327px;top:138px;width:546px;height:945px;
    background:var(--notice-grey);overflow:hidden;
    box-shadow:0 6px 30px rgba(0,0,0,.18);
  }

  /* status bar */
  .status-bar{position:absolute;left:0;top:0;width:100%;height:40px;background:var(--status-grey);
    display:flex;align-items:center;padding:0 12px 0 8px;color:var(--ink);font-size:13px}
  .app-icon{width:20px;height:20px;border-radius:4px;background:#1a3f9e;margin-right:7px}
  .app-name{flex:1;letter-spacing:.2px}
  .show-more{font-size:13px}

  /* notification */
  .notification{position:absolute;left:14px;top:48px;color:var(--ink);font-size:15px;line-height:16px}
  .notification-title{font-weight:700;margin-bottom:3px}
  .notification-close{position:absolute;left:453px;top:49px;width:46px;height:46px;border-radius:50%;
    background:var(--blue-action);color:var(--white);font-weight:700;font-size:24px;
    display:flex;align-items:center;justify-content:center}

  /* header */
  .post-header{position:absolute;left:0;top:111px;width:100%;height:180px;background:var(--pink);
    border-radius:56px 56px 0 0}
  .post-title{position:absolute;left:47px;top:40px;color:var(--white);font-size:37px;font-weight:500;letter-spacing:.3px}
  .privacy-toggle{position:absolute;left:372px;top:40px;width:124px;height:39px;border-radius:20px;
    background:var(--white);display:flex;align-items:center;padding-left:15px;color:var(--pink);font-size:21px}
  .privacy-toggle svg{position:absolute;right:3px;top:3px}

  /* compose area */
  .compose{position:absolute;left:0;top:222px;width:100%;height:306px;background:var(--white);
    border-radius:50px 50px 0 0}
  .compose-placeholder{position:absolute;left:51px;top:42px;font-size:26px;color:var(--placeholder)}
  .compose-cursor{position:absolute;left:46px;top:48px;width:2px;height:25px;background:var(--blue)}
  .emoji-button{position:absolute;left:448px;top:236px;width:56px;text-align:center;color:var(--pink-accent);font-size:15px}
  .emoji-button svg{display:block;margin:0 auto 3px}

  /* action bar */
  .action-bar{position:absolute;left:0;top:528px;width:100%;height:103px;background:var(--blue)}
  .send-button{position:absolute;left:223px;top:475px;width:100px;height:100px;border-radius:50%;background:var(--white);
    display:flex;align-items:center;justify-content:center}
  .send-button span{width:74px;height:74px;border-radius:50%;background:var(--blue-action);display:flex;align-items:center;justify-content:center}
  .action{position:absolute;top:0;width:110px;margin-left:-55px;text-align:center;color:var(--white);font-size:14px}
  .action svg{display:block;margin:0 auto 4px}

  /* keyboard */
  .keyboard{position:absolute;left:0;top:631px;width:100%;height:314px;background:var(--kb-bg)}
  .key-row{position:absolute;left:4px;right:5px;display:flex;justify-content:space-between}
  .key{height:60px;border-radius:8px;background:var(--key);color:var(--white);
    display:flex;align-items:center;justify-content:center;font-size:29px}
  .key.letter{width:45px}
  .key.fn{background:var(--key-fn)}
  .row-1{top:11px}
  .row-2{top:89px;left:31px;right:32px}
  .row-3{top:167px}
  .row-3 .letters{display:flex;gap:9.5px}
  .row-4{top:243px;font-size:22px}
  .row-4 .key{font-size:22px}
</style>
</head>
<body>
<main class="phone-screen">
  <div class="status-bar">
    <span class="app-icon"></span>
    <span class="app-name">APP NAME</span>
    <span class="show-more">Show More</span>
  </div>

  <div class="notification">
    <p class="notification-title">Notification (Selected)</p>
    <p>Notification content can go here.</p>
    <p>You can edit this text freely</p>
  </div>
  <div class="notification-close">X</div>

  <section class="post-header">
    <h1 class="post-title">Create Post</h1>
    <div class="privacy-toggle">Private
      <svg width="33" height="33" viewBox="0 0 33 33">
        <circle cx="16.5" cy="16.5" r="15.5" fill="var(--pink)"/>
        <g stroke="var(--blue)" stroke-width="1.8" stroke-linecap="round">
          <line x1="16.5" y1="4" x2="16.5" y2="12"/><line x1="16.5" y1="21" x2="16.5" y2="29"/>
          <line x1="4" y1="16.5" x2="12" y2="16.5"/><line x1="21" y1="16.5" x2="29" y2="16.5"/>
          <line x1="7.7" y1="7.7" x2="13.3" y2="13.3"/><line x1="19.7" y1="19.7" x2="25.3" y2="25.3"/>
          <line x1="25.3" y1="7.7" x2="19.7" y2="13.3"/><line x1="13.3" y1="19.7" x2="7.7" y2="25.3"/>
        </g>
      </svg>
    </div>
  </section>

  <section class="compose">
    <span class="compose-cursor"></span>
    <p class="compose-placeholder">Share a new post</p>
    <div class="emoji-button">
      <svg width="34" height="34" viewBox="0 0 34 34" fill="none" stroke="var(--pink-accent)" stroke-width="1.6">
        <circle cx="17" cy="17" r="15.5"/>
        <circle cx="11.5" cy="13" r="1.4" fill="var(--pink-accent)" stroke="none"/>
        <circle cx="22.5" cy="13" r="1.4" fill="var(--pink-accent)" stroke="none"/>
        <path d="M10 20.5c3.5 4 10.5 4 14 0" stroke-linecap="round"/>
      </svg>
      Emojis
    </div>
  </section>

  <nav class="action-bar">
    <div class="action" style="left:62px;top:38px">
      <svg width="36" height="27" viewBox="0 0 36 27" fill="var(--white)">
        <path d="M8 0h26v21h-3V3H8z"/>
        <rect x="0" y="5" width="29" height="21" rx="3"/>
      </svg>Add photos</div>
    <div class="action" style="left:175px;top:36px">
      <svg width="20" height="30" viewBox="0 0 20 30">
        <path d="M10 0C4.5 0 0 4.3 0 9.8 0 17 10 30 10 30s10-13 10-20.2C20 4.3 15.5 0 10 0z" fill="var(--white)"/>
        <circle cx="10" cy="9.5" r="3.6" fill="var(--blue)"/>
      </svg>Check-In</div>
    <div class="action" style="left:379px;top:35px">
      <svg width="28" height="28" viewBox="0 0 28 28">
        <circle cx="14" cy="14" r="13" fill="none" stroke="var(--white)" stroke-width="1.6"/>
        <circle cx="14" cy="10.5" r="4.8" fill="var(--white)"/>
        <path d="M7 24c0-5 3-8 7-8s7 3 7 8z" fill="var(--white)"/>
      </svg>Tag Friends</div>
    <div class="action" style="left:492px;top:35px">
      <svg width="28" height="28" viewBox="0 0 28 28" fill="none" stroke="var(--white)" stroke-width="1.6" stroke-linecap="round">
        <path d="M20 9 9.5 19.5a2.5 2.5 0 0 1-3.5-3.5L18 4a4.3 4.3 0 0 1 6 6L11 23a6 6 0 0 1-8.5-8.5L13 4"/>
      </svg>Add files</div>
  </nav>

  <div class="send-button"><span>
    <svg width="34" height="26" viewBox="0 0 34 26"><path d="M0 0 34 13 0 26 5 13z" fill="var(--white)"/><path d="M5 13h14" stroke="var(--blue-action)" stroke-width="2"/></svg>
  </span></div>

  <section class="keyboard" aria-label="Keyboard">
    <div class="key-row row-1">
      <span class="key letter">q</span><span class="key letter">w</span><span class="key letter">e</span><span class="key letter">r</span><span class="key letter">t</span><span class="key letter">y</span><span class="key letter">u</span><span class="key letter">i</span><span class="key letter">o</span><span class="key letter">p</span>
    </div>
    <div class="key-row row-2">
      <span class="key letter">a</span><span class="key letter">s</span><span class="key letter">d</span><span class="key letter">f</span><span class="key letter">g</span><span class="key letter">h</span><span class="key letter">j</span><span class="key letter">k</span><span class="key letter">l</span>
    </div>
    <div class="key-row row-3">
      <span class="key fn" style="width:61px">
        <svg width="30" height="26" viewBox="0 0 30 26" fill="none" stroke="var(--white)" stroke-width="1.4" stroke-linejoin="round"><path d="M15 2 2 15h7v9h12v-9h7z"/></svg>
      </span>
      <div class="letters">
        <span class="key letter">z</span><span class="key letter">x</span><span class="key letter">c</span><span class="key letter">v</span><span class="key letter">b</span><span class="key letter">n</span><span class="key letter">m</span>
      </div>
      <span class="key fn" style="width:61px">
        <svg width="32" height="24" viewBox="0 0 32 24" fill="none" stroke="var(--white)" stroke-width="1.4" stroke-linejoin="round"><path d="M10 2h20v20H10L1 12z"/><path d="M15 7l10 10M25 7 15 17"/></svg>
      </span>
    </div>
    <div class="key-row row-4">
      <span class="key fn" style="width:58px">123</span>
      <span class="key fn" style="width:60px">
        <svg width="30" height="30" viewBox="0 0 30 30" fill="none" stroke="var(--white)" stroke-width="1.8"><circle cx="15" cy="15" r="13"/><circle cx="10.5" cy="11.5" r="1.5" fill="var(--white)" stroke="none"/><circle cx="19.5" cy="11.5" r="1.5" fill="var(--white)" stroke="none"/><path d="M8 16h14c0 4-3 7-7 7s-7-3-7-7z"/></svg>
      </span>
      <span class="key fn" style="width:45px;background:var(--key)">
        <svg width="20" height="30" viewBox="0 0 20 30" fill="none" stroke="var(--white)" stroke-width="1.6" stroke-linecap="round"><rect x="6" y="1" width="8" height="17" rx="4"/><path d="M2 13c0 5 3.5 8 8 8s8-3 8-8M10 21v6M6 28h8"/></svg>
      </span>
      <span class="key" style="width:209px">space</span>
      <span class="key fn" style="width:127px">return</span>
    </div>
  </section>
</main>
</body>
</html>
```